Ridge Gathering presented by The Keystone

This is a one-day seminar for men who want to grow mentally, spiritually and financially.
Host Pastor Darnell Whitford
Special guest: Dr. Vernon Blake, Dr. Simone Harker

Target Market(s)

Men 18-55

Colors

Designer to choose colors to be used in the design.

Requirements
Must have
• clean designs
Nice to have
• A clean design that translates to social media and websites

```html
<!DOCTYPE html>
<html lang="en">
<head>
<meta charset="utf-8">
<title>Ridge Gathering — The Keystone</title>
<link href="https://fonts.googleapis.com/css2?family=Montserrat:wght@400;600;700;800&display=swap" rel="stylesheet">
<style>
  :root {
    --red: #c01e2e;
    --ink: #262526;
    --band: #2b2a2b;
    --grey: #9a9a9a;
    --crowd-light: #f1f1f1;
    --crowd-mid: #d9d9d9;
    --paper: #ffffff;
  }
  * { margin: 0; padding: 0; box-sizing: border-box; }
  html, body { width: 889px; height: 1200px; overflow: hidden; background: var(--paper); }
  .poster {
    position: relative; width: 889px; height: 1200px; overflow: hidden;
    background: var(--paper);
    font-family: "Montserrat", Arial, sans-serif;
    color: var(--ink);
  }
  .frame-lines { position: absolute; inset: 0; z-index: 3; pointer-events: none; }
  .crowd-backdrop {
    position: absolute; left: 0; top: 600px; width: 889px; height: 370px;
    background: linear-gradient(180deg, rgba(255,255,255,0) 0%, var(--crowd-light) 40%, var(--crowd-mid) 100%);
    z-index: 0;
  }
  .dark-band {
    position: absolute; left: 0; top: 955px; width: 889px; height: 245px;
    background: var(--band); z-index: 1;
  }
  .event-title {
    position: absolute; top: 24px; width: 100%; text-align: center; z-index: 4;
    color: var(--red); font-weight: 800; font-size: 35px; letter-spacing: -0.5px;
  }
  .presented-by {
    position: absolute; top: 68px; width: 100%; text-align: center; z-index: 4;
    font-size: 15px; letter-spacing: 5px; font-weight: 600; color: var(--ink);
  }
  .brand {
    position: absolute; top: 235px; width: 100%; display: flex; justify-content: center;
    align-items: center; gap: 22px; z-index: 4;
  }
  .brand-name { font-size: 92px; font-weight: 700; color: var(--ink); letter-spacing: -3px; }
  .brand-dot { width: 34px; height: 34px; border-radius: 50%; background: var(--red); }
  .pillars {
    position: absolute; top: 474px; width: 100%; text-align: center; z-index: 4;
    color: var(--red); font-weight: 700; font-size: 28px; letter-spacing: -0.8px;
  }
  .intro {
    position: absolute; top: 557px; left: 207px; width: 500px; z-index: 4;
    font-size: 27px; font-weight: 400; letter-spacing: -0.3px;
  }
  .intro strong { color: var(--red); font-weight: 800; }
  .growth { position: absolute; top: 596px; left: 203px; z-index: 4; }
  .growth-line {
    display: block; font-weight: 800; font-size: 68px; line-height: 62px;
    letter-spacing: -2.5px; text-transform: uppercase;
  }
  .tone-grey { color: var(--grey); }
  .tone-red { color: var(--red); }
  .tone-ink { color: var(--ink); }
  .speakers {
    position: absolute; top: 848px; left: 0; width: 889px; z-index: 4;
    display: flex; justify-content: center; gap: 57px;
  }
  .speaker { width: 202px; text-align: center; }
  .speaker-photo {
    width: 202px; height: 202px; border-radius: 50%;
    border: 9px solid var(--red);
    background: radial-gradient(circle at 50% 45%, #c9c3bd 0%, #8d8580 60%, #5e5754 100%);
  }
  .speaker-name {
    margin-top: 22px; color: var(--red); font-weight: 800; font-size: 19px;
    line-height: 26px; letter-spacing: -0.4px; text-transform: uppercase; white-space: nowrap;
  }
  .speaker-name.single { margin-top: 48px; }
  .speaker-role { color: var(--paper); font-size: 19px; line-height: 28px; }
</style>
</head>
<body>
<main class="poster">
  <div class="crowd-backdrop" role="img" aria-label="Faint grey silhouettes of an audience and a speaker holding a microphone"></div>
  <div class="dark-band"></div>

  <svg class="frame-lines" width="889" height="1200" viewBox="0 0 889 1200">
    <g stroke="#c01e2e" stroke-width="2" fill="none">
      <polyline points="268,57 41,57 41,955"/>
      <polyline points="621,57 848,57 848,955"/>
      <polyline points="256,546 256,535 636,535"/>
      <polyline points="256,797 256,808 636,808 636,797"/>
    </g>
    <g stroke="#ffffff" stroke-width="2" fill="none">
      <polyline points="41,955 41,1162 848,1162 848,955"/>
    </g>
  </svg>

  <h1 class="event-title">RIDGE GATHERING</h1>
  <p class="presented-by">PRESENTED BY</p>

  <div class="brand">
    <span class="brand-name">The Keystone</span>
    <span class="brand-dot"></span>
  </div>

  <p class="pillars">MANHOOD BROTHERHOOD SERVANTHOOD</p>

  <p class="intro">For Those Who wants to <strong>GROW</strong></p>
  <h2 class="growth">
    <span class="growth-line"><span class="tone-grey">Men</span><span class="tone-red">tally</span></span>
    <span class="growth-line tone-ink">Spiritually</span>
    <span class="growth-line"><span class="tone-red">Finan</span><span class="tone-ink">cially</span></span>
  </h2>

  <section class="speakers">
    <article class="speaker">
      <div class="speaker-photo" role="img" aria-label="Portrait photo of host Pastor Darnell Whitford"></div>
      <p class="speaker-name">Pastor<br>Darnell Whitford</p>
      <p class="speaker-role">Host</p>
    </article>
    <article class="speaker">
      <div class="speaker-photo" role="img" aria-label="Portrait photo of special guest Dr. Vernon Blake"></div>
      <p class="speaker-name single">Dr. Vernon Blake</p>
      <p class="speaker-role">Special Guest</p>
    </article>
    <article class="speaker">
      <div class="speaker-photo" role="img" aria-label="Portrait photo of special guest Dr. Simone Harker"></div>
      <p class="speaker-name single">Dr. Simone Harker</p>
      <p class="speaker-role">Special Guest</p>
    </article>
  </section>
</main>
</body>
</html>
```